Want a package created for a new protein bar

We would like a new package created for a new protein bar project The name of the bar will be VOLMBite a real food protein bar, we would like a ‘window’ on the package of bar like Brave Meadow bar below in images.

VOLMBite
‘Super Food Bar’
14g of Whey Protein
The package film size is the following 12cm width x 15cm Length,
Flavor Peanut Chocolate Chip, additional information will be attached shortly like nutrition facts,

Target Market(s)

fitness market, bodybuilders, athletes, everyday people

Industry/Entity Type

Health Product

Logo Text

VOLMBite

Font styles to use
Serif
Sans Serif
Decorative

Requirements
Must have
• Package window

```html
<!DOCTYPE html>
<html lang="en">
<head>
<meta charset="utf-8">
<title>VOLMBite Protein Bar Wrapper</title>
<link rel="stylesheet" href="https://fonts.googleapis.com/css2?family=Oswald:wght@600&family=Roboto+Condensed:wght@400;700&display=swap">
<style>
  :root {
    --backdrop: #bba544;
    --wrapper-red: #b3122a;
    --wrapper-red-dark: #8e0c1f;
    --wrapper-yellow: #f2d20f;
    --wrapper-yellow-light: #f8e24a;
    --crimp-black: #2a2a2a;
    --bar-brown: #7c4f26;
    --bar-brown-light: #a5703a;
    --peanut-tan: #d9a766;
    --ink: #2b1408;
    --white: #ffffff;
  }
  html, body {
    margin: 0;
    padding: 0;
    width: 1200px;
    height: 960px;
    overflow: hidden;
    background: var(--backdrop);
  }
  .canvas {
    position: relative;
    width: 1200px;
    height: 960px;
  }
  .wrapper {
    position: absolute;
    left: 60px;
    top: 360px;
    width: 1080px;
    height: 240px;
  }
  .wrapper-shapes {
    position: absolute;
    inset: 0;
  }
  .brand-name {
    position: absolute;
    left: 150px;
    top: 12px;
    margin: 0;
    font-family: "Oswald", sans-serif;
    font-weight: 600;
    font-size: 86px;
    line-height: 1;
    letter-spacing: 2px;
    color: var(--wrapper-yellow);
  }
  .tagline {
    position: absolute;
    left: 250px;
    top: 136px;
    margin: 0;
    font-family: "Roboto Condensed", sans-serif;
    font-weight: 700;
    font-size: 25px;
    line-height: 1;
    color: var(--ink);
  }
  .flavor {
    position: absolute;
    left: 500px;
    top: 176px;
    margin: 0;
    font-family: "Roboto Condensed", sans-serif;
    font-weight: 400;
    font-size: 16px;
    line-height: 1.1;
    color: var(--wrapper-red);
    text-transform: uppercase;
  }
  .protein-amount {
    position: absolute;
    left: 86px;
    top: 176px;
    width: 100px;
    margin: 0;
    font-family: "Roboto Condensed", sans-serif;
    color: var(--white);
    text-align: center;
    line-height: 1;
  }
  .protein-amount .grams {
    display: block;
    font-size: 30px;
  }
  .protein-amount .label {
    display: block;
    font-size: 12px;
    font-weight: 700;
    margin-top: 4px;
  }
</style>
</head>
<body>
<main class="canvas">
  <section class="wrapper" aria-label="VOLMBite protein bar wrapper, flat layout">
    <svg class="wrapper-shapes" width="1080" height="240" viewBox="0 0 1080 240">
      <defs>
        <linearGradient id="barFill" x1="0" y1="0" x2="1" y2="1">
          <stop offset="0" stop-color="var(--bar-brown-light)"/>
          <stop offset="1" stop-color="var(--bar-brown)"/>
        </linearGradient>
      </defs>
      <polygon class="crimp-left" fill="var(--crimp-black)" points="70,0 70,240 0,240 6,228 0,216 6,204 0,192 6,180 0,168 6,156 0,144 6,132 0,120 6,108 0,96 6,84 0,72 6,60 0,48 6,36 0,24 6,12 0,0"/>
      <polygon class="crimp-right" fill="var(--wrapper-red)" points="1010,0 1010,240 1080,240 1074,228 1080,216 1074,204 1080,192 1074,180 1080,168 1074,156 1080,144 1074,132 1080,120 1074,108 1080,96 1074,84 1080,72 1074,60 1080,48 1074,36 1080,24 1074,12 1080,0"/>
      <rect class="body-red" x="70" y="0" width="940" height="240" fill="var(--wrapper-red)"/>
      <polygon class="body-yellow" fill="var(--wrapper-yellow)" points="200,128 630,112 630,240 200,240"/>
      <rect class="name-underlay" x="150" y="128" width="50" height="40" fill="var(--wrapper-yellow-light)"/>
      <rect class="accent-stripe" x="70" y="0" width="560" height="8" fill="var(--wrapper-red-dark)"/>
      <rect class="side-panel" x="830" y="0" width="180" height="240" fill="var(--wrapper-yellow)"/>
      <rect class="window" role="img" aria-label="Window showing the peanut chocolate chip protein bar" x="630" y="0" width="200" height="240" fill="url(#barFill)"/>
      <ellipse class="peanut-art" role="img" aria-label="Illustration of peanuts with leaves" cx="420" cy="196" rx="48" ry="30" fill="var(--peanut-tan)"/>
      <g class="diet-marks" fill="none" stroke="var(--ink)" stroke-width="2">
        <circle cx="920" cy="40" r="17"/>
        <circle cx="920" cy="92" r="17"/>
        <circle cx="920" cy="144" r="17"/>
        <circle cx="920" cy="196" r="17"/>
      </g>
    </svg>
    <h1 class="brand-name">VOLMBITE</h1>
    <p class="tagline">Super Food PROTEIN Bar</p>
    <p class="flavor">Flavor Peanut<br>Chocolate Chip</p>
    <p class="protein-amount"><span class="grams">14g</span><span class="label">WHEY PROTEIN</span></p>
  </section>
</main>
</body>
</html>
```